vellar.com music website

I need a graphic designer to help me design a very modern looking theme for vellar.com, a website for sharing songs. I currently have a very ugly old-looking design that I want to replace. I need a great logo, a great page theme. Just one comp is all I need of the home page. Must have two tag lines: "it pays to share" and "get paid to share music" The current design has all the elements I need, so I have attached it as a download. vellar is pronounced vehlar. the current site is not live. Please feel free to send me questions.
Updates

Reason: I want to give everyone a chance to get their design in. Thank you.

Target Market(s)

The site needs to appeal to music fans that will be pulled in by the concept of "it pays to share," as well as the pop of the design. It has to look fun and cool. Empahsis on modern looking design.

Industry/Entity Type

Graphic Designer

Requirements
Must have
• engaging logo, there must be a container that holds video, scrolls right and left. 6 action buttons, for Plumora, Zendrol, My, Add, Search, More. You can put the first letter only on the buttons. Must have two tag lines: "it pays to share" and "get paid to share music" Please include the elements, such as login, join, etc... that are in the comp that you can download. Obviously I don't want it to look like what I already have, except that it must have a container that holds the video. The container that holds the video has to have the same aspect ratio that kobrastream uses for it's embed codes. You can find this ratio by checking any kobrastream video embed code, they have a custom size tool which lets you play with the sizes. Any question, pls contact thanks.
Nice to have
• unlike the existing comp, it can have white space. Just looking for a good modern theme with a cool logo. Jquery style themes might be nice... Also, think along the lines of a cool techy feel for mobile...

This is a cool image, but obviously don't get too close to it because it belongs to another music site:

http://kpnoverbyte2011.files.brindlehost.com/2012/03/capture-2012-03-28-at-12-02-36-pm.png?w=194

```html
<!DOCTYPE html>
<html lang="en">
<head>
<meta charset="utf-8">
<title>vellar.com — it pays to share</title>
<link href="https://fonts.googleapis.com/css2?family=Lato:wght@300;400;700&display=swap" rel="stylesheet">
<style>
:root{
  --bg:#f1f1f1;
  --ink:#2b2b2b;
  --muted:#6b6b6b;
  --green:#35963a;
  --green-soft:#5cae5f;
  --player:#1b1b1b;
  --player-dim:#7a7a7a;
  --red:#c8201f;
  --white:#ffffff;
}
*{box-sizing:border-box;margin:0;padding:0}
html,body{width:1200px;height:977px;overflow:hidden;background:var(--bg)}
body{font-family:"Lato",Arial,sans-serif;color:var(--ink)}
.canvas{position:relative;width:1200px;height:977px;overflow:hidden;background:var(--bg)}

.brand{position:absolute;left:84px;top:0;width:508px;height:72px;background:linear-gradient(90deg,#e6e6e6,#dcdcdc);display:flex;align-items:center;padding-left:80px}
.brand-name{font-size:40px;font-weight:700;color:var(--green)}
.top-nav{position:absolute;top:27px;left:852px;display:flex;gap:52px}
.top-nav a{font-size:25px;font-weight:300;color:var(--ink);text-decoration:none}

.video-rail{position:absolute;top:92px;left:0;width:1200px;height:486px}
.video{position:absolute;top:0;height:486px;background:#000;overflow:hidden}
.video.side{background:var(--player-dim)}
.video.side .screen{opacity:.55}
.video.prev{left:0;width:194px}
.video.main{left:203px;width:815px}
.video.next{left:1028px;width:172px}
.screen{position:absolute;top:0;left:0;right:0;bottom:33px;background:#000}
.screen-art{position:absolute;top:0;bottom:0;left:102px;width:513px;background:linear-gradient(100deg,#3a3a3a,#bdbdbd 35%,#6e6e6e 60%,#d0d0d0 75%,#2c2c2c)}
.controls{position:absolute;left:0;right:0;bottom:0;height:33px;background:linear-gradient(#2a2a2a,#141414);color:#ddd;font-size:11px}
.side .controls{background:linear-gradient(#8a8a8a,#777)}
.progress{position:absolute;top:-4px;left:0;right:0;height:5px;background:#3a3a3a}
.progress i{position:absolute;left:0;top:0;height:5px;width:45px;background:var(--red)}
.progress b{position:absolute;left:39px;top:-3px;width:12px;height:12px;border-radius:50%;background:#eee}
.controls svg{position:absolute;top:9px}
.time{position:absolute;left:96px;top:10px}
.time span{color:#999}

.arrow{position:absolute;top:277px;width:83px;height:83px;border-radius:50%;background:var(--green)}
.arrow svg{position:absolute;top:0;left:0}
.arrow.left{left:162px}
.arrow.right{left:969px}

.share-bar{position:absolute;top:588px;left:394px;display:flex;gap:14px}
.share-btn{width:60px;height:60px;border-radius:50%;display:flex;align-items:center;justify-content:center;color:var(--white);font-size:11px;font-weight:700;border:2px solid rgba(0,0,0,.25)}
.s-sonara{background:#c82121}
.s-plumora{background:#2c5a9a}
.s-delvo{background:#1f4f8f}
.s-zendrol{background:#2a8fb0}
.s-postly{background:#ef7d16}
.s-kobra{background:#9a9a9a}

.tagline{position:absolute;top:670px;left:0;width:1200px;text-align:center;font-size:29px;font-weight:300;color:var(--ink)}
.subline{position:absolute;top:714px;left:0;width:1200px;text-align:center;font-size:18px;font-weight:300;color:var(--muted)}

.panel{position:absolute;top:774px;height:86px;background:var(--green);border:1px solid #2c8631;border-radius:2px;color:var(--white);padding:11px 10px}
.tweet{left:154px;width:438px;font-size:14px;font-weight:300;line-height:23px}
.tweet a{color:var(--white)}
.tweet small{display:block;font-size:11px;line-height:20px}
.newsletter{left:611px;width:439px;font-size:15px}
.newsletter form{display:flex;gap:10px;margin-top:10px}
.newsletter input{width:340px;height:34px;border:0;padding:0 6px;font:700 13px "Lato",Arial,sans-serif;color:#666}
.newsletter button{width:70px;height:34px;border:0;background:var(--green-soft);color:var(--white);font:400 15px "Lato",Arial,sans-serif}

.footer-nav{position:absolute;top:914px;left:154px;font-size:14px;letter-spacing:2px;color:#777}
.footer-nav a{color:#777;text-decoration:none}
.footer-nav .sep{margin:0 6px}
.footer-social{position:absolute;top:913px;left:949px;display:flex;gap:7px}
.footer-social span{width:21px;height:21px;border-radius:50%;background:var(--green-soft)}
.copyright{position:absolute;top:946px;left:154px;font-size:10px;font-weight:300;color:#aaa}
</style>
</head>
<body>
<div class="canvas">
  <header>
    <div class="brand"><span class="brand-name">vellar</span></div>
    <nav class="top-nav"><a href="#">JOIN</a><a href="#">LOGIN</a></nav>
  </header>

  <section class="video-rail">
    <div class="video side prev">
      <div class="screen" role="img" aria-label="Previous music video still"></div>
      <div class="controls"><div class="progress"></div></div>
    </div>
    <div class="video main">
      <div class="screen"><div class="screen-art" role="img" aria-label="Music video still: black and white title frame"></div></div>
      <div class="controls">
        <div class="progress"><i></i><b></b></div>
        <svg width="16" height="16" style="left:22px"><path d="M3 2l11 6-11 6z" fill="#ccc"/></svg>
        <svg width="22" height="16" style="left:64px"><path d="M2 5h4l5-4v14l-5-4H2z" fill="#ccc"/><path d="M14 4q4 4 0 8" stroke="#ccc" fill="none"/></svg>
        <div class="time">0:11 <span>/ 3:50</span></div>
        <svg width="16" height="16" style="left:706px"><circle cx="8" cy="8" r="5" fill="none" stroke="#ccc" stroke-width="3"/></svg>
        <svg width="16" height="16" style="left:736px"><circle cx="8" cy="8" r="7" fill="#ccc"/></svg>
        <svg width="18" height="16" style="left:765px"><rect x="2" y="4" width="14" height="9" fill="none" stroke="#ccc" stroke-width="2"/></svg>
        <svg width="20" height="16" style="left:794px"><rect x="2" y="3" width="16" height="11" fill="none" stroke="#ccc" stroke-width="2"/></svg>
        <svg width="18" height="16" style="left:826px"><path d="M1 5V1h4M13 1h4v4M17 11v4h-4M5 15H1v-4" fill="none" stroke="#ccc" stroke-width="2"/></svg>
      </div>
    </div>
    <div class="video side next">
      <div class="screen" role="img" aria-label="Next music video still"></div>
      <div class="controls">
        <div class="progress"><i></i><b></b></div>
        <div class="time">0:11 <span>/ 3:50</span></div>
      </div>
    </div>
    <a class="arrow left" href="#" aria-label="Previous video"><svg width="83" height="83"><path d="M22 42l30-18v36z" fill="#fff"/></svg></a>
    <a class="arrow right" href="#" aria-label="Next video"><svg width="83" height="83"><path d="M61 42L31 24v36z" fill="#fff"/></svg></a>
  </section>

  <nav class="share-bar">
    <a class="share-btn s-sonara">Sonara</a>
    <a class="share-btn s-plumora">Plumora</a>
    <a class="share-btn s-delvo">Delvo</a>
    <a class="share-btn s-zendrol">Zendrol</a>
    <a class="share-btn s-postly">Postly</a>
    <a class="share-btn s-kobra">kobra</a>
  </nav>

  <h1 class="tagline">it pays to share</h1>
  <p class="subline">In vellar Get paid to share music, each kobrastream music video you share u will get paid etc or learn more</p>

  <div class="panel tweet">
    Music is life, and life is money so start now and get paid to share music <a href="#">@Brellik</a> <a href="#">@Vellar</a> <a href="#">http://qz.io/etc</a>
    <small>Posted March 29th, 2012</small>
  </div>
  <div class="panel newsletter">
    Sign up for our newsletter
    <form><input type="text" placeholder="Signup for our newsletter" value="Signup for our newsletter"><button type="button">Send</button></form>
  </div>

  <footer>
    <nav class="footer-nav"><a href="#">HOME</a><span class="sep">/</span><a href="#">ABOUT</a><span class="sep">/</span><a href="#">TERMS</a><span class="sep">/</span><a href="#">PRIVACY</a><span class="sep">/</span><a href="#">SUPPORT</a></nav>
    <div class="footer-social"><span></span><span></span><span></span><span></span></div>
    <p class="copyright">2012 vellar share media, US etc something</p>
  </footer>
</div>
</body>
</html>
```